Design a "healthy, happy dog and cat" cheque/check background

I am looking for a few design concepts featuring a happy healthy dog and cat, that will be used as the background of a paper cheque/check.

This will require Photoshop and stock photos.

Here is the design brief: https://files.brieflocker.net/d/8Xq3LmTz0wRcYvNb2KpHsJfGdUeAi5oWnQ/view?share=link

Colors

Requirements
Must have
• A happy dog and cat the main focus within the "empty" central part of the cheque/check, and a complementary background for the rest of the cheque, following the design guidelines in the attached google doc.

```html
<!DOCTYPE html>
<html lang="en">
<head>
<meta charset="utf-8">
<title>Dog and Cat Personal Cheque</title>
<link rel="stylesheet" href="https://fonts.googleapis.com/css2?family=Arimo:wght@400;700&family=Share+Tech+Mono&display=swap">
<style>
  :root {
    --backdrop: #000000;
    --paper: #ffffff;
    --cheque-tint: #eef5d5;
    --ink: #2b2b2b;
    --ink-soft: #444444;
    --rule: #555555;
    --fur-warm: #d6a565;
    --fur-cool: #b9b2ad;
  }
  html, body {
    margin: 0;
    padding: 0;
    width: 1200px;
    height: 1000px;
    overflow: hidden;
    background: var(--backdrop);
    font-family: "Arimo", Arial, sans-serif;
    color: var(--ink);
  }
  .canvas { position: relative; width: 1200px; height: 1000px; }
  .cheque-sheet {
    position: absolute; left: 30px; top: 233px; width: 1117px; height: 507px;
    background: var(--paper);
  }
  .cheque-face {
    position: absolute; left: 52px; top: 253px; width: 1095px; height: 367px;
    background: var(--cheque-tint);
  }
  .pet-artwork {
    position: absolute; left: 365px; top: 262px; width: 455px; height: 358px;
    background: linear-gradient(90deg, rgba(214,165,101,0) 0%, var(--fur-warm) 20%, var(--fur-warm) 48%, var(--fur-cool) 62%, var(--fur-cool) 85%, rgba(185,178,173,0) 100%);
    border-radius: 45% 45% 6px 6px / 30% 30% 6px 6px;
    opacity: .85;
  }
  .abs { position: absolute; white-space: nowrap; }
  .account-holder { left: 82px; top: 290px; font-size: 19px; line-height: 21px; color: var(--ink-soft); }
  .account-holder strong { font-weight: 700; }
  .cheque-number { left: 982px; top: 277px; font-size: 24px; font-weight: 700; color: #000; }
  .date-label { left: 759px; top: 336px; font-size: 17px; color: var(--ink); }
  .date-boxes { left: 820px; top: 318px; display: flex; gap: 3px; }
  .date-boxes span { width: 34px; height: 34px; background: var(--paper); }
  .date-format { left: 820px; top: 355px; display: flex; gap: 3px; font-size: 13px; }
  .date-format span { width: 34px; text-align: center; }
  .payee-label { left: 82px; top: 411px; font-size: 13px; line-height: 13px; color: var(--ink-soft); }
  .currency-sign { left: 911px; top: 406px; font-size: 28px; }
  .amount-box { left: 936px; top: 397px; width: 178px; height: 44px; background: var(--paper); }
  .amount-words { left: 884px; top: 468px; font-size: 14px; }
  .bank-mark { left: 88px; top: 503px; width: 70px; height: 70px; border-radius: 50%; background: var(--ink); }
  .bank-details { left: 172px; top: 512px; font-size: 17px; line-height: 18px; color: #111; }
  .bank-details strong { font-weight: 700; }
  .company-name { left: 782px; top: 544px; font-size: 13px; color: #111; }
  .memo-label { left: 86px; top: 590px; font-size: 12px; color: var(--ink-soft); }
  .security-note {
    left: 1110px; top: 487px; width: 28px; height: 124px;
    border: 1px solid var(--rule); box-sizing: border-box;
  }
  .security-text {
    position: absolute; left: 3px; top: 60px; transform: rotate(-90deg); transform-origin: left top;
    font-size: 7px; line-height: 8px; color: var(--ink-soft);
  }
  .security-badge { position: absolute; left: 5px; top: 108px; width: 16px; height: 12px; background: var(--ink-soft); }
  .micr-line { left: 80px; top: 650px; font-family: "Share Tech Mono", monospace; font-size: 28px; letter-spacing: 1px; color: #111; }
  .rules { position: absolute; left: 0; top: 0; }
</style>
</head>
<body>
<main class="canvas">
  <div class="cheque-sheet"></div>
  <div class="cheque-face"></div>
  <div class="pet-artwork" role="img" aria-label="Puppy nuzzling a grey kitten, photographed together in the centre of the cheque"></div>

  <svg class="rules" width="1200" height="1000" aria-hidden="true">
    <g stroke="var(--rule)" stroke-width="1.2" fill="none">
      <line x1="82" y1="440" x2="888" y2="440"/>
      <line x1="888" y1="414" x2="888" y2="440"/>
      <line x1="82" y1="490" x2="870" y2="490"/>
      <line x1="870" y1="490" x2="880" y2="460"/>
      <line x1="86" y1="604" x2="1052" y2="604"/>
    </g>
    <g fill="var(--ink-soft)">
      <rect x="1117" y="567" width="14" height="11" rx="1"/>
      <path d="M1120 567v-4a4 4 0 0 1 8 0v4" stroke="var(--ink-soft)" stroke-width="1.6" fill="none"/>
    </g>
  </svg>

  <div class="abs account-holder"><strong>Maplewood Cheque Co. Personal Cheque</strong><br>15 Residential Street<br>Toronto, Ontario M1M 1M1</div>
  <div class="abs cheque-number">101</div>

  <div class="abs date-label">DATE</div>
  <div class="abs date-boxes"><span></span><span></span><span></span><span></span><span></span><span></span><span></span><span></span></div>
  <div class="abs date-format"><span>D</span><span>D</span><span>M</span><span>M</span><span>Y</span><span>Y</span><span>Y</span><span>Y</span></div>

  <div class="abs payee-label">PAY TO THE<br>ORDER OF</div>
  <div class="abs currency-sign">$</div>
  <div class="abs amount-box"></div>
  <div class="abs amount-words">100 DOLLARS</div>

  <div class="abs bank-mark"></div>
  <div class="abs bank-details"><strong>Your Financial Institution</strong><br>200 Finance Avenue<br>Your City, Your Province A1B 2CS</div>
  <div class="abs company-name">Optional Company Name</div>
  <div class="abs memo-label">MEMO</div>

  <div class="abs security-note">
    <div class="security-text">Details on Back<br>Détails au Verso</div>
    <div class="security-badge"></div>
  </div>

  <div class="abs micr-line">⑈101⑈ ⑆12345⑉678⑆ 12345⑉6789⑈</div>
</main>
</body>
</html>
```